Velder Auto Repair - Flyer Design

My business is a automobile shop where we fix cars. Such things that we do but not limited to is brakes, Engine/Transmission change, Electrical work, emission test, oil change and automobile diagnostic. I am looking for a flyer that will catch peoples attention, I will be giving flyers to people, putting them in car windows and mailboxes. I am looking for a flier that will help to attract more customers to my business. I also want the flyer to say "Bring in your estimate from our competitors with this flyer and we will beat it by 10%" (does not have to be in those exact words). I also want the flyer to have my business address phone and operating hours. I have attached a business card and my business ad which I have placed in the newspaper before. I hope it helps with your design.
Industry/Entity Type
Car Repair
Look and feel

```html
<!DOCTYPE html>
<html lang="en">
<head>
<meta charset="utf-8">
<title>Velder Auto Repair – Flyer</title>
<link rel="stylesheet" href="https://fonts.googleapis.com/css2?family=Chivo:wght@400;700;900&family=Lily+Script+One&display=swap">
<style>
  :root {
    --ink: #0d0d0d;
    --paper: #ffffff;
    --metal-light: #cfd3d4;
    --metal-mid: #b9bdbc;
    --rust: #b98a66;
    --rust-dark: #9c6a48;
    --patina: #8fa38a;
    --car-fill: #e9e9e7;
  }
  * { margin: 0; padding: 0; box-sizing: border-box; }
  html, body { width: 881px; height: 1200px; overflow: hidden; }
  body { background: var(--metal-light); }

  .flyer {
    position: relative;
    width: 881px;
    height: 1200px;
    overflow: hidden;
    color: var(--ink);
    font-family: "Chivo", Arial, sans-serif;
  }

  .backdrop {
    position: absolute;
    inset: 0;
    background:
      radial-gradient(ellipse 420px 360px at 760px 220px, rgba(185,138,102,.75), transparent 70%),
      radial-gradient(ellipse 380px 300px at 140px 90px, rgba(185,138,102,.55), transparent 70%),
      radial-gradient(ellipse 420px 380px at 820px 980px, rgba(156,106,72,.5), transparent 70%),
      radial-gradient(ellipse 360px 300px at 120px 1050px, rgba(143,163,138,.55), transparent 70%),
      radial-gradient(ellipse 300px 260px at 700px 560px, rgba(143,163,138,.35), transparent 70%),
      linear-gradient(160deg, var(--metal-light), var(--metal-mid));
  }

  .car-illustration {
    position: absolute;
    left: 28px;
    top: 76px;
    width: 808px;
    height: 364px;
    border-radius: 120px 160px 90px 90px / 80px 120px 60px 60px;
    background: linear-gradient(180deg, var(--car-fill), #cfcfcc);
    box-shadow: inset 0 0 0 4px var(--ink);
  }

  .name-badge {
    position: absolute;
    left: 64px;
    top: 452px;
    width: 736px;
    height: 208px;
  }
  .name-badge svg { position: absolute; inset: 0; }

  .business-name {
    position: absolute;
    left: 0; right: 0;
    top: 50px;
    text-align: center;
    font-weight: 900;
    font-size: 55px;
    letter-spacing: 1px;
    line-height: 1;
    text-shadow: 2px 3px 4px rgba(0,0,0,.35);
  }
  .specialty {
    position: absolute;
    left: 0; right: 0;
    top: 112px;
    text-align: center;
    font-weight: 700;
    font-size: 26px;
    line-height: 40px;
    letter-spacing: 1px;
  }

  .price-promise {
    position: absolute;
    left: 0; right: 0;
    top: 694px;
    text-align: center;
    font-family: "Lily Script One", cursive;
    font-size: 38px;
    line-height: 54px;
  }

  .contact {
    position: absolute;
    left: 0; right: 0;
    top: 878px;
    text-align: center;
    font-size: 28px;
    line-height: 40px;
    letter-spacing: 1px;
  }
  .contact .email {
    font-size: 17px;
    line-height: 30px;
    margin-top: 2px;
  }

  .hours {
    position: absolute;
    left: 0; right: 0;
    top: 1056px;
    text-align: center;
    font-size: 18px;
    line-height: 27px;
    letter-spacing: 1px;
  }
</style>
</head>
<body>
<main class="flyer">
  <div class="backdrop" role="img" aria-label="Weathered rusty metal texture with faded green brush strokes"></div>

  <div class="car-illustration" role="img" aria-label="Line illustration of a classic 1950s convertible car"></div>

  <section class="name-badge">
    <svg viewBox="0 0 736 208" width="736" height="208" aria-hidden="true">
      <path fill="#0d0d0d" d="M240 0 H496 V14 H700 A22 22 0 0 0 716 36 C736 70 736 138 716 172 A22 22 0 0 0 700 194 H496 V208 H240 V194 H36 A22 22 0 0 0 20 172 C0 138 0 70 20 36 A22 22 0 0 0 36 14 H240 Z"/>
      <path fill="#ffffff" stroke="#0d0d0d" stroke-width="3" d="M250 12 H486 V26 H690 A20 20 0 0 0 704 42 C718 76 718 132 704 166 A20 20 0 0 0 690 182 H486 V196 H250 V182 H46 A20 20 0 0 0 32 166 C18 132 18 76 32 42 A20 20 0 0 0 46 26 H250 Z"/>
    </svg>
    <h1 class="business-name">Velder Auto Repair</h1>
    <p class="specialty">Specializing in<br>Foreign &amp; Domestic Cars</p>
  </section>

  <p class="price-promise">Bring in your estimate from our<br>competitors with this flyer and<br>we will beat it by 10%!</p>

  <address class="contact" style="font-style:normal">
    <div>4127 S. Harbor Ave</div>
    <div>Chicago, IL. 60609</div>
    <div>(773) 555-0148</div>
    <div class="email">Email: VelderAutoRepair@mailbox.com</div>
  </address>

  <section class="hours">
    <div>Hours of Operation</div>
    <div>Monday to Friday: 8am-5pm</div>
    <div>Saturday: 8am-1pm</div>
    <div>Sunday: CLOSED</div>
  </section>
</main>
</body>
</html>
```